Business Card Design

Need a hot business card in wine colors something cool and mod please feel free to be , FUNKY and free with this .

Industry/Entity Type

Business

Contact Information for Business Card

LUMERA HAIR DESIGN 3182 w 9th st scottsdale az 85619 Custom modern hair design and custom color by MARCUS OBRIDGE 602-4168203 cell salon 480 -712-6084 email marcusobridge@quillpost.com hours wed thru sat 7am to 6pm.

Font styles to use
Other font styles liked:
• something fun and mod.

Colors
a54599
6b449b
1b1b1b
606060

Requirements
Must have
• Apointment reminder on flip side of card.
Should not have
• Nothing boring.

```html
<!DOCTYPE html>
<html lang="en">
<head>
<meta charset="utf-8">
<title>Lumera Hair Design – Business Card</title>
<link rel="stylesheet" href="https://fonts.googleapis.com/css2?family=Open+Sans:wght@400;600;700&display=swap">
<style>
  :root {
    --ink: #1b1b1b;
    --ink-soft: #2b2a2b;
    --grey: #606060;
    --orchid: #a54599;
    --violet: #6b449b;
    --paper: #ffffff;
    --stage: #e7e4e1;
    --body-font: "Open Sans", sans-serif;
  }
  * { box-sizing: border-box; margin: 0; padding: 0; }
  html, body {
    width: 1200px; height: 800px; overflow: hidden;
    background: var(--stage);
    font-family: var(--body-font);
  }
  .stage { position: relative; width: 1200px; height: 800px; }

  .card {
    position: absolute; top: 120px;
    width: 320px; height: 560px;
    border-radius: 16px; overflow: hidden;
    background: var(--ink);
    color: var(--paper);
    box-shadow: 0 10px 28px rgba(0,0,0,.28);
  }
  .card--front { left: 250px; }
  .card--back {
    left: 630px;
    background: linear-gradient(160deg, var(--ink-soft), var(--ink) 60%);
  }

  /* Front: appointment reminder */
  .front-name {
    position: absolute; left: 24px; top: 16px;
    font-size: 14px; font-weight: 600; letter-spacing: 1.5px;
    white-space: nowrap;
  }
  .front-artwork {
    position: absolute; left: 40px; top: 52px; right: 0; bottom: 36px;
    border-radius: 120px 0 0 0;
    background:
      radial-gradient(circle at 65% 22%, rgba(165,69,153,.35), transparent 38%),
      radial-gradient(circle at 75% 42%, rgba(107,68,155,.25), transparent 30%),
      linear-gradient(180deg, #f3eef3, var(--paper) 55%);
  }
  .appointment {
    position: absolute; left: 100px; right: 28px; bottom: 72px;
    color: var(--ink);
  }
  .appointment-row {
    display: flex; align-items: flex-end; gap: 6px;
    font-weight: 700; font-size: 17px; margin-top: 8px;
  }
  .appointment-line { flex: 1; border-bottom: 1px solid var(--ink); height: 16px; }

  /* Back: contact side */
  .tagline {
    position: absolute; top: 36px; left: 0; right: 0;
    text-align: center; font-size: 13px; line-height: 1.45;
  }
  .contact {
    position: absolute; top: 130px; right: 28px; left: 28px;
    text-align: right;
  }
  .contact-name { font-weight: 700; font-size: 17px; letter-spacing: .5px; }
  .contact-rule { border: 0; border-top: 1px solid var(--grey); margin: 8px 0 8px 40px; }
  .contact-line {
    display: flex; justify-content: flex-end; align-items: center; gap: 7px;
    font-size: 14px; margin-top: 3px;
  }
  .contact-line svg { width: 15px; height: 15px; flex: none; }
  .contact-email {
    position: absolute; top: 262px; left: 28px;
    display: flex; align-items: center; gap: 7px; font-size: 14px;
  }
  .contact-email svg { width: 16px; height: 13px; }
  .brand {
    position: absolute; right: 28px; top: 400px;
    display: flex; align-items: center; gap: 10px;
  }
  .brand-dot { width: 12px; height: 12px; border-radius: 50%; background: var(--orchid); flex: none; }
  .brand-name {
    font-size: 18px; font-weight: 600; letter-spacing: 1.5px;
    white-space: nowrap;
  }
  .address {
    position: absolute; bottom: 30px; left: 0; right: 0;
    text-align: center; font-size: 14px; letter-spacing: .3px;
  }
</style>
</head>
<body>
<main class="stage">

  <section class="card card--front" aria-label="Appointment reminder side">
    <p class="front-name">LUMERA HAIR DESIGN</p>
    <div class="front-artwork" role="img" aria-label="White silhouette illustration of a woman's profile with flowing hair and purple swirls and dotted flowers"></div>
    <div class="appointment">
      <div class="appointment-row">Date: <span class="appointment-line"></span></div>
      <div class="appointment-row">Time: <span class="appointment-line"></span></div>
    </div>
  </section>

  <section class="card card--back" aria-label="Contact side">
    <p class="tagline">Custom modern hair design<br>and<br>custom color by:</p>

    <div class="contact">
      <p class="contact-name">MARCUS OBRIDGE</p>
      <hr class="contact-rule">
      <p class="contact-line">
        <svg viewBox="0 0 16 16" aria-hidden="true"><rect x="1" y="1" width="14" height="14" rx="2" fill="#fff"/><rect x="5" y="3" width="6" height="10" rx="1" fill="#1b1b1b"/><rect x="6" y="4" width="4" height="6" fill="#fff"/></svg>
        602-4168203
      </p>
      <p class="contact-line">
        <svg viewBox="0 0 16 16" aria-hidden="true"><rect x="1" y="1" width="14" height="14" rx="2" fill="#fff"/><path d="M5 4c-1 1-1 3 1 5s4 3 5 2l1-1-2-2-1 1c-1 0-2-1-2-2l1-1-2-2z" fill="#1b1b1b"/></svg>
        480-712-6084
      </p>
    </div>

    <p class="contact-email">
      <svg viewBox="0 0 16 13" aria-hidden="true"><rect x="0.5" y="0.5" width="15" height="12" rx="1.5" fill="#fff"/><path d="M1.5 2l6.5 5 6.5-5" stroke="#1b1b1b" stroke-width="1.4" fill="none"/></svg>
      marcusobridge@quillpost.com
    </p>

    <div class="brand">
      <span class="brand-dot" aria-hidden="true"></span>
      <p class="brand-name">LUMERA HAIR DESIGN</p>
    </div>

    <p class="address">3182 w 9th st scottsdale az 85619</p>
  </section>

</main>
</body>
</html>
```